Need Business Cards for my Business

email address: klmvertexcalibration@mailcove.com
web address: klmvertexcalibration.com
Slogan: We offer various NRB licenses
Wallace R. Pendry
Please stick with colors of Company Logo
would like the card to be more of the color example of the logo.
If you need PDF copy of logo email me at the above account.
Creative control rests with you.

Industry/Entity Type

Business

Contact Information for Business Card

I am a minimalist, but would like something to pop and stand out amongst other cards, make it memorable.

Font styles to use
Serif
Decorative
Script

```html
<!DOCTYPE html>
<html lang="en">
<head>
<meta charset="utf-8">
<title>Vertex Calibration — Business Card</title>
<link rel="stylesheet" href="https://fonts.googleapis.com/css2?family=Open+Sans:wght@400;600;700&display=swap">
<style>
  :root {
    --navy: #163a6b;
    --red: #d42634;
    --ink: #2d2d2d;
    --black: #151515;
    --white: #ffffff;
    --backdrop: #e9e9ea;
  }
  * { margin: 0; padding: 0; box-sizing: border-box; }
  html, body { width: 1200px; height: 900px; overflow: hidden; }
  body {
    background: var(--backdrop);
    font-family: "Open Sans", Arial, sans-serif;
    position: relative;
  }
  .card {
    position: absolute;
    width: 640px;
    height: 366px;
    overflow: hidden;
    box-shadow: 0 6px 18px rgba(0,0,0,0.18);
  }
  .card-back {
    left: 500px; top: 50px;
    background: var(--black);
    display: flex; align-items: center; justify-content: center;
  }
  .card-back .wordmark {
    color: var(--white);
    font-weight: 700;
    font-size: 36px;
    letter-spacing: 5px;
    text-transform: uppercase;
  }
  .card-front { left: 60px; top: 460px; background: var(--white); }
  .card-front .shapes { position: absolute; inset: 0; }
  .name {
    position: absolute; left: 66px; top: 36px;
    font-size: 21px; font-weight: 700; color: var(--navy);
  }
  .name .first { color: var(--red); }
  .contacts {
    position: absolute; left: 50px; top: 150px;
    list-style: none; font-size: 16px; color: var(--ink); line-height: 23px;
  }
  .contacts li { display: flex; align-items: center; gap: 10px; }
  .contacts svg { width: 13px; height: 13px; fill: var(--navy); flex: none; }
  .slogan {
    position: absolute; left: 50px; top: 246px;
    font-size: 16px; color: var(--navy); text-transform: uppercase; letter-spacing: 0.3px;
  }
  .brand {
    position: absolute; left: 420px; top: 150px;
    display: flex; align-items: center; gap: 10px;
  }
  .brand .dot { width: 18px; height: 18px; border-radius: 50%; background: var(--red); flex: none; }
  .brand .brand-name {
    font-size: 21px; font-weight: 700; color: var(--navy);
    text-transform: uppercase; letter-spacing: 1.5px; line-height: 1.15;
  }
</style>
</head>
<body>
  <section class="card card-back">
    <span class="wordmark">Vertex Calibration</span>
  </section>

  <section class="card card-front">
    <svg class="shapes" viewBox="0 0 640 366" width="640" height="366" aria-hidden="true">
      <polygon points="0,0 34,0 0,26" fill="var(--red)"/>
      <polygon points="40,0 56,0 56,30 6,30" fill="var(--navy)"/>
      <polygon points="0,300 296,300 282,320 0,320" fill="var(--red)"/>
      <polygon points="312,300 640,300 640,346 280,346" fill="var(--navy)"/>
    </svg>

    <h1 class="name"><span class="first">Wallace</span> R. Pendry</h1>

    <ul class="contacts">
      <li>
        <svg viewBox="0 0 24 24"><path d="M6.6 10.8a15.1 15.1 0 0 0 6.6 6.6l2.2-2.2a1 1 0 0 1 1-.25 11.4 11.4 0 0 0 3.6.57 1 1 0 0 1 1 1V20a1 1 0 0 1-1 1A17 17 0 0 1 3 4a1 1 0 0 1 1-1h3.5a1 1 0 0 1 1 1c0 1.25.2 2.45.57 3.57a1 1 0 0 1-.25 1z"/></svg>
        415-555-0183
      </li>
      <li>
        <svg viewBox="0 0 24 24"><path d="M2 5h20v14H2z"/><path d="M3 6.5l9 6.5 9-6.5" stroke="#fff" stroke-width="1.6" fill="none"/></svg>
        klmvertexcalibration@mailcove.com
      </li>
      <li>
        <svg viewBox="0 0 24 24"><circle cx="12" cy="12" r="10"/><path d="M2 12h20M12 2c3 3 3 17 0 20M12 2c-3 3-3 17 0 20" stroke="#fff" stroke-width="1.4" fill="none"/></svg>
        klmvertexcalibration.com
      </li>
    </ul>

    <p class="slogan">We offer various NRB licenses</p>

    <div class="brand">
      <span class="dot"></span>
      <span class="brand-name">Vertex<br>Calibration</span>
    </div>
  </section>
</body>
</html>
```